Vesk Architecture

We are a architectural design and build company working between scales 1/1000 to 1/1 we want people to understand our difference from our design experience and quality.we build hotels restourants and office spaces.Our company name is Vesk architecture to mind sustainability.

We want to write our adress phone and work spesifications on the card and we want our logo as backround.

Ps:you could find the logo adress and phone box numbers from the web:www.veskmimarlik-ornek.com

Target Market(s)

Who looks for experts.

Industry/Entity Type

Architecture

Requirements
Must have
• Design is over everything.
Should not have
• we don want it to be colorfull

```html
<!DOCTYPE html>
<html lang="tr">
<head>
<meta charset="utf-8">
<title>Vesk Architecture – Business Card</title>
<link href="https://fonts.googleapis.com/css2?family=Montserrat:ital,wght@0,400;1,400;1,600&family=Cormorant+Garamond:wght@500&display=swap" rel="stylesheet">
<style>
  :root {
    --page-bg: #d6d6d6;
    --card-bg: #f1f1f1;
    --card-edge: #e6e6e6;
    --band-bg: #dcdcdc;
    --ink: #111111;
    --ink-soft: #222222;
    --rule: #333333;
    --icon: #2f5483;
    --label: #3a3a3a;
  }
  * { margin: 0; padding: 0; box-sizing: border-box; }
  html, body { width: 1200px; height: 895px; overflow: hidden; }
  body {
    background: var(--page-bg);
    position: relative;
    font-family: "Montserrat", Arial, sans-serif;
  }
  .card {
    position: absolute;
    top: 302px;
    width: 570px;
    height: 343px;
    border-radius: 16px;
    background: radial-gradient(ellipse at 50% 45%, #fafafa 0%, var(--card-bg) 55%, var(--card-edge) 100%);
    overflow: hidden;
  }
  .card--front { left: 18px; }
  .card--back { left: 611px; }

  .wordmark {
    position: absolute;
    color: var(--ink);
    font-weight: 400;
    line-height: 1;
    text-align: left;
  }
  .wordmark__name { display: block; letter-spacing: 1px; }
  .wordmark__sub { display: block; letter-spacing: 2px; }

  .card--front .wordmark { left: 206px; top: 108px; }
  .card--front .wordmark__name { font-size: 76px; }
  .card--front .wordmark__sub { font-size: 19px; margin-top: 4px; }

  .card--back .band {
    position: absolute;
    left: 0; right: 0; bottom: 0;
    height: 64px;
    background: var(--band-bg);
    border-top: 1px solid #cfcfcf;
  }
  .card--back .divider {
    position: absolute;
    left: 356px; top: 98px;
    width: 2px; height: 162px;
    background: var(--rule);
  }
  .card--back .wordmark { left: 374px; top: 136px; }
  .card--back .wordmark__name { font-size: 62px; }
  .card--back .wordmark__sub { font-size: 16px; margin-top: 3px; }

  .contact {
    position: absolute;
    right: 230px;
    top: 149px;
    text-align: right;
    font-style: italic;
    color: var(--ink-soft);
    font-size: 13px;
    line-height: 17px;
  }
  .contact__street { font-weight: 600; color: var(--ink); }
  .contact__list { list-style: none; position: absolute; right: 0; top: 34px; width: 320px; }
  .contact__item { display: flex; justify-content: flex-end; align-items: center; gap: 10px; height: 17px; }
  .contact__item svg { width: 18px; height: 14px; flex: none; margin-right: -30px; }

  .view-label {
    position: absolute;
    top: 685px;
    font-family: "Cormorant Garamond", Georgia, serif;
    font-size: 16px;
    letter-spacing: 3px;
    color: var(--label);
  }
  .view-label--front { left: 66px; }
  .view-label--back { left: 659px; }
</style>
</head>
<body>

<section class="card card--front" aria-label="Card front">
  <div class="wordmark">
    <span class="wordmark__name">vesk</span>
    <span class="wordmark__sub">MİMARLIK</span>
  </div>
</section>

<section class="card card--back" aria-label="Card back">
  <div class="contact">
    <p class="contact__street">Yeldegirmeni Mah. Ornek Cad. Lale Sok</p>
    <p>No.7 Ornek Kadikoy Istanbul</p>
    <ul class="contact__list">
      <li class="contact__item"><span>0216 555 01 23</span>
        <svg viewBox="0 0 18 14" aria-hidden="true"><rect x="1" y="5" width="16" height="8" rx="2" fill="var(--icon)"/><path d="M2 5 Q9 -1 16 5" stroke="var(--icon)" stroke-width="2.4" fill="none"/><circle cx="9" cy="9" r="2" fill="#fff"/></svg>
      </li>
      <li class="contact__item"><span>0216 555 01 61</span>
        <svg viewBox="0 0 18 14" aria-hidden="true"><rect x="1" y="2" width="16" height="11" rx="3" fill="var(--icon)"/><rect x="3" y="6" width="12" height="3" fill="#fff"/></svg>
      </li>
      <li class="contact__item"><span>veskmimarlik@ornek-posta.com</span>
        <svg viewBox="0 0 18 14" aria-hidden="true"><rect x="1" y="2" width="16" height="11" fill="var(--icon)"/><path d="M1 2 L9 9 L17 2" stroke="#fff" stroke-width="1.5" fill="none"/></svg>
      </li>
    </ul>
  </div>
  <div class="divider"></div>
  <div class="wordmark">
    <span class="wordmark__name">vesk</span>
    <span class="wordmark__sub">MİMARLIK</span>
  </div>
  <div class="band"></div>
</section>

<p class="view-label view-label--front">FRONT</p>
<p class="view-label view-label--back">BACK</p>

</body>
</html>
```